Fleyer für Rasenroboter-Garage
Zielgruppe
Aluminiumsysteme
Aufgabenstellung
Für ein neues Produkt " Rasenroboter-Garage" einen Fleyer entwerfen. Format DinA4 Vorder und Rückseite. Bilder der Garage sind als Anhang anbei.Es gibt eine Basic Version mit Dach und eine Expert Version mit Dach und Seitenverkleidung. Sogan " Das Zuhause für Ihren Rasenroboter" . Merkmale sind hochertige Materialien, qualitative Verarbeitung, ästhetisches Design,lange Lebensdauer.

```html
<!DOCTYPE html>
<html lang="de">
<head>
<meta charset="utf-8">
<title>MOWNEST – Das Zuhause für Ihren Rasen-Roboter</title>
<link rel="stylesheet" href="https://fonts.googleapis.com/css2?family=Arimo:wght@400;700&family=Audiowide&family=Kaushan+Script&family=Oswald:wght@500;700&display=swap">
<style>
  :root {
    --stage: #1c1c1c;
    --paper: #ffffff;
    --ink: #1a1a1a;
    --text: #333333;
    --green: #8cc63f;
    --green-dark: #5f9424;
    --black: #0d0d0d;
    --sky: #7fb2e0;
    --meadow: #4e9a2a;
  }
  * { box-sizing: border-box; margin: 0; padding: 0; }
  html, body { width: 1200px; height: 942px; overflow: hidden; }
  body { background: var(--stage); font-family: "Arimo", Arial, sans-serif; }

  .flyer {
    position: absolute; left: 280px; top: 18px;
    width: 640px; height: 906px;
    background: var(--paper); overflow: hidden;
  }

  /* hero */
  .hero {
    position: absolute; left: 0; top: 0; width: 640px; height: 330px;
    background: linear-gradient(180deg, var(--sky) 0%, #cfe6f5 30%, #9ccc62 48%, var(--meadow) 75%, #2f6e18 100%);
  }
  .brand {
    position: absolute; left: 130px; top: 22px; width: 280px; height: 78px;
    background: var(--black); display: flex; align-items: center; justify-content: center; gap: 12px;
  }
  .brand-mark { width: 16px; height: 16px; background: var(--green); }
  .brand-name { font-family: "Audiowide", sans-serif; color: var(--green); font-size: 30px; letter-spacing: 2px; }

  .slogan {
    position: absolute; left: 24px; top: 222px; width: 360px;
    font-family: "Kaushan Script", cursive; color: #ffffff; font-size: 36px; line-height: 1.05;
    text-shadow: 0 2px 4px rgba(0,0,0,.5);
  }
  .hero-rule { position: absolute; left: 0; top: 330px; width: 640px; height: 8px; background: var(--black); }

  /* price badges */
  .badge {
    position: absolute; width: 120px; height: 120px; border-radius: 50%;
    background: var(--black); border: 4px solid #ffffff; box-shadow: 0 3px 8px rgba(0,0,0,.45);
    overflow: hidden; text-align: center; color: #ffffff;
  }
  .badge-label { font-family: "Audiowide", sans-serif; font-size: 13px; line-height: 16px; letter-spacing: 1px; margin-top: 16px; }
  .badge-price {
    background: var(--green); margin-top: 5px; padding: 2px 0;
    font-family: "Oswald", sans-serif; font-weight: 700; font-size: 34px; line-height: 1.1;
  }
  .badge-note { font-size: 7px; font-weight: 700; text-transform: uppercase; margin: 3px 18px 0; line-height: 1.15; }
  .badge-premium { left: 468px; top: 38px; }
  .badge-frame { left: 503px; top: 390px; }
  .badge-casing { left: 503px; top: 546px; }

  /* products */
  .product-shot { position: absolute; border-radius: 2px; }
  .shot-frame { left: 345px; top: 380px; width: 190px; height: 110px;
    background: linear-gradient(180deg, #3f6e68 0%, #2b4f4b 35%, #e9e9e9 36%, #ffffff 100%); }
  .shot-casing { left: 345px; top: 540px; width: 190px; height: 120px;
    background: linear-gradient(160deg, #5e8f86 0%, #3b655f 60%, #2a4a45 100%); }

  .specs { position: absolute; left: 30px; top: 370px; width: 300px; color: var(--text); }
  .spec-block + .spec-block { margin-top: 26px; }
  .spec-title { font-family: "Audiowide", sans-serif; font-size: 13px; color: var(--ink); margin-bottom: 8px; }
  .spec-text { font-size: 11px; line-height: 1.4; margin-bottom: 6px; }
  .spec-key { font-weight: 700; color: var(--green); text-transform: uppercase; }
  .spec-line { font-size: 11px; margin-bottom: 6px; }

  /* ticker */
  .ticker {
    position: absolute; left: 0; top: 712px; width: 640px; height: 28px;
    background: var(--black); color: #ffffff; display: flex; align-items: center; justify-content: center;
    font-family: "Oswald", sans-serif; font-weight: 500; font-size: 13px; letter-spacing: .4px; white-space: nowrap;
  }

  /* contact footer */
  .contact { position: absolute; left: 0; top: 740px; width: 640px; height: 166px; background: var(--green); }
  .phone-row { position: absolute; left: 30px; top: 30px; display: flex; align-items: center; gap: 16px; }
  .phone-icon { width: 40px; height: 40px; }
  .phone-number { font-family: "Oswald", sans-serif; font-weight: 700; font-size: 44px; color: var(--ink); }
  .web-line {
    position: absolute; left: 30px; top: 110px; width: 580px;
    font-family: "Oswald", sans-serif; font-weight: 500; font-size: 13px; letter-spacing: .5px; color: #ffffff;
    text-transform: uppercase;
  }
</style>
</head>
<body>
<main class="flyer">
  <section class="hero" role="img" aria-label="Foto: Rasenroboter unter einer Aluminium-Garage auf einer Wiese mit blauem Himmel">
    <div class="brand"><span class="brand-mark"></span><span class="brand-name">MOWNEST</span></div>
    <p class="slogan">Das Zuhause für<br>Ihren Rasen-Roboter</p>
  </section>
  <div class="hero-rule"></div>

  <div class="badge badge-premium">
    <p class="badge-label">PREMIUM</p>
    <p class="badge-price">229,-</p>
    <p class="badge-note">Komplettset mit Dach</p>
  </div>

  <div class="product-shot shot-frame" role="img" aria-label="Foto: Garagen-Gestell mit Dach über einem Rasenroboter"></div>
  <div class="badge badge-frame">
    <p class="badge-label">GESTELL</p>
    <p class="badge-price">99,-</p>
    <p class="badge-note">Nur Dach ohne Roboter</p>
  </div>

  <div class="product-shot shot-casing" role="img" aria-label="Foto: geschlossenes Garagen-Gehäuse mit Seitenverkleidung"></div>
  <div class="badge badge-casing">
    <p class="badge-label">GEHÄUSE</p>
    <p class="badge-price">229,-</p>
    <p class="badge-note">Gehäuse ohne Roboter</p>
  </div>

  <section class="specs">
    <article class="spec-block">
      <h2 class="spec-title">PRODUKTBESCHREIBUNG GESTELL</h2>
      <p class="spec-text"><span class="spec-key">Material:</span> Die äußerst stabile Garage ist aus hochwertigem Aluminium gefertigt, der Montage-Befestigungssatz besteht aus rostfreiem Stahl und bietet hervorragenden Schutz gegen alle Umwelteinflüsse, Balleinschläge usw...</p>
      <p class="spec-line"><span class="spec-key">Abmessungen:</span> 1445 x 1525 x Höhe 820 mm</p>
      <p class="spec-line"><span class="spec-key">Gewicht:</span> 35 kg</p>
    </article>
    <article class="spec-block">
      <h2 class="spec-title">PRODUKTBESCHREIBUNG GEHÄUSE</h2>
      <p class="spec-text"><span class="spec-key">Material:</span> Die äußerst stabile Garage ist aus hochwertigem Aluminium gefertigt, der Montage-Befestigungssatz besteht aus rostfreiem Stahl und bietet hervorragenden Schutz gegen alle Umwelteinflüsse, Balleinschläge usw...</p>
      <p class="spec-line"><span class="spec-key">Abmessungen:</span> 1445 x 1525 x Höhe 820 mm</p>
      <p class="spec-line"><span class="spec-key">Gewicht:</span> 50 kg</p>
    </article>
  </section>

  <div class="ticker">NUR SOLANGE DER VORRAT REICHT +++ BESTELLEN SIE GLEICH HEUTE +++ NUR SOLANGE DER VORRAT REICHT</div>

  <footer class="contact">
    <div class="phone-row">
      <svg class="phone-icon" viewBox="0 0 40 40" aria-hidden="true">
        <path d="M6 14c0-4 3-7 14-7s14 3 14 7v3h-8v-4c-2-1-4-1-6-1s-4 0-6 1v4H6z" fill="#ffffff"/>
        <path d="M12 19h16l4 14H8z" fill="#ffffff"/>
        <circle cx="20" cy="26" r="4" fill="var(--green)"/>
      </svg>
      <span class="phone-number">+ 49 (0) 321 - 98 76 54 00</span>
    </div>
    <p class="web-line">To get more information of this program please visit our website: www.mownest-garage.de</p>
  </footer>
</main>
</body>
</html>
```